Project Management Consultancy needs logo, business card and stationary design

I need a logo, business card and stationary design for a start-up project management consultancy servicing clients in corporate, education, aviation, local government and construction sectors.

The business will provide professional advice to clients and our people, knowledge and experience is essentially what we sell.

Our role is to assist our clients in delivering successful construction and transition projects whilst ensuring that their needs are identified, understood and achieved.

The company is small and provides a tailor made service for our clients. We pride ourselves on being
- professional
- innovative
- collaborative
- dependable
- communicative
- confident
- bold
The logo, business card and stationary should reflect this.

Can you please include the following on the stationary as appropriate.
Address:
27 Melverton Crescent
Coledale
NSW 2748

ABN: 42 873 306 129

I very much look forward to receiving your designs.

Greg T.

Target Market(s)

Corporate clients such as: airports, universities, government, financial organisations, etc.

Industry/Entity Type

Management Consulting

Contact Information for Business Card

Greg Tolliver
Director
Tolliver Management Consulting Pty Ltd
e. greg.tolliver@tolliver-mc.com.au
m. +61 438 590 163

Font styles to use
Other font styles liked:
• perhaps Arial Narrow? I am open to suggestions

Requirements
Must have
• An dynamic and corporate look and feel.
Should not have
• Should not be boring.

```html
<!DOCTYPE html>
<html lang="en">
<head>
<meta charset="utf-8">
<title>Tolliver Management Consulting – Business Cards</title>
<link href="https://fonts.googleapis.com/css2?family=Open+Sans:wght@400;600;700&display=swap" rel="stylesheet">
<style>
  :root {
    --backdrop: #3a332e;
    --card: #0d0d0d;
    --blue: #2a7cc6;
    --silver: #b9b9b9;
    --text: #d4d4d4;
    --rule: #3a3a3a;
  }
  * { margin: 0; padding: 0; box-sizing: border-box; }
  html, body {
    width: 1200px; height: 900px; overflow: hidden;
    background: var(--backdrop);
    font-family: "Open Sans", Arial, sans-serif;
  }
  .stage { position: relative; width: 1200px; height: 900px; }
  .card {
    position: absolute;
    width: 510px; height: 310px;
    background: var(--card);
    border-radius: 3px;
    box-shadow: 0 12px 30px rgba(0,0,0,0.45);
  }
  /* Contact side */
  .card--contact { left: 60px; top: 295px; }
  .contact-brand {
    position: absolute; left: 38px; top: 200px;
    display: flex; align-items: center; gap: 12px;
  }
  .brand-square { width: 22px; height: 22px; background: var(--blue); }
  .brand-name {
    font-size: 30px; font-weight: 600; letter-spacing: 2px;
    color: var(--silver);
  }
  .divider {
    position: absolute; left: 232px; top: 60px;
    width: 1px; height: 190px; background: var(--rule);
  }
  .details {
    position: absolute; left: 252px; top: 58px;
    color: var(--text); font-size: 13px; line-height: 1.35;
  }
  .person-name { color: var(--blue); font-weight: 700; font-size: 16px; }
  .person-role { margin-bottom: 14px; }
  .abn { margin-bottom: 14px; }
  .abn-label { color: var(--blue); font-weight: 700; }
  .address { margin-bottom: 8px; }
  .contact-line { display: flex; align-items: center; gap: 8px; }
  .contact-line svg { flex: none; }

  /* Logo side */
  .card--logo { left: 630px; top: 295px; }
  .logo-lockup {
    position: absolute; inset: 0;
    display: flex; flex-direction: column; align-items: center; justify-content: center;
    color: var(--silver);
  }
  .logo-name { font-size: 54px; font-weight: 400; letter-spacing: 6px; line-height: 1; }
  .logo-tagline { font-size: 20px; font-weight: 400; letter-spacing: 1px; margin-top: 8px; }
</style>
</head>
<body>
<div class="stage">

  <section class="card card--contact">
    <div class="contact-brand">
      <span class="brand-square"></span>
      <span class="brand-name">TOLLIVER</span>
    </div>
    <div class="divider"></div>
    <div class="details">
      <p class="person-name">Greg Tolliver</p>
      <p class="person-role">Director</p>
      <p class="abn"><span class="abn-label">ABN:</span> 42 873 306 129</p>
      <p class="address">27 Melverton Crescent<br>Brackenwood VIC 3748</p>
      <p class="contact-line">
        <svg width="9" height="12" viewBox="0 0 9 12" aria-hidden="true"><rect x="0.75" y="0.75" width="7.5" height="10.5" rx="1.2" fill="none" stroke="#2a7cc6" stroke-width="1.5"/><circle cx="4.5" cy="9.3" r="0.8" fill="#2a7cc6"/></svg>
        +61 438 590 163
      </p>
      <p class="contact-line">
        <svg width="11" height="9" viewBox="0 0 11 9" aria-hidden="true"><rect width="11" height="9" rx="1" fill="#2a7cc6"/><path d="M0.5 1 L5.5 5 L10.5 1" fill="none" stroke="#0d0d0d" stroke-width="1.2"/></svg>
        greg.tolliver@tolliver-mc.com.au
      </p>
    </div>
  </section>

  <section class="card card--logo">
    <div class="logo-lockup">
      <span class="logo-name">TOLLIVER</span>
      <span class="logo-tagline">Management Consulting</span>
    </div>
  </section>

</div>
</body>
</html>
```